Junk Removal company with existing WordPress website needs new mobile enhanced website

I am looking to have someone take my existing website and either update it with a new design and menu which is more mobile enhanced (70% of my traffic is from mobile devices and most people stay on the home page to find what they need) or create a new website from scratch to achieve my design goals. My name goal is the have to home page be quick and easy to find what the customer is looking for.
Our current website is: BrightCreekJunkOut.com and Google my business page https://g.page/brightcreekjunkout
I have attached an example the design idea I came up with for the home page based on what I would like it to look like as well as some logo files and pictures.

```html
<!DOCTYPE html>
<html lang="en">
<head>
<meta charset="utf-8">
<title>Bright Creek Junk Out – Home Page Desktop and Mobile</title>
<link href="https://fonts.googleapis.com/css2?family=Roboto:wght@400;500;700;900&display=swap" rel="stylesheet">
<style>
:root{
  --orange:#f26a0a;
  --orange-dark:#d95400;
  --ink:#141414;
  --text:#444;
  --muted:#777;
  --grey:#ececec;
  --stage:#f4f4f4;
  --white:#fff;
}
*{box-sizing:border-box;margin:0;padding:0}
html,body{width:1200px;height:5172px;overflow:hidden}
body{background:var(--stage);font-family:"Roboto",Arial,sans-serif;color:var(--text);position:relative}
.desktop{position:absolute;left:28px;top:20px;width:812px;height:5140px;background:var(--white);box-shadow:0 2px 10px rgba(0,0,0,.12);overflow:hidden}
.mobile{position:absolute;left:884px;top:20px;width:270px;height:5010px;background:var(--white);box-shadow:0 2px 10px rgba(0,0,0,.12);overflow:hidden}
section,header,footer{position:absolute;left:0;width:100%}
.ph{background:linear-gradient(135deg,#8a7460,#4f4337);}
.ph.cool{background:linear-gradient(135deg,#6f7c88,#3c4650)}
.ph.light{background:linear-gradient(135deg,#c9c2b8,#8e8478)}
.ph.dark{background:linear-gradient(135deg,#3a3a3a,#1a1a1a)}
.ph.map{background:linear-gradient(135deg,#e8e4da,#cfd8c8)}
.btn{display:inline-block;background:var(--ink);color:var(--white);font-size:9px;font-weight:700;letter-spacing:.5px;padding:8px 18px;text-transform:uppercase}
.btn.orange{background:var(--orange)}
.h2{font-size:26px;font-weight:700;color:var(--ink);text-align:center;text-transform:uppercase}
.small{font-size:8px;line-height:1.5;color:var(--text)}
.center{text-align:center}

/* header */
.site-header{top:0;height:120px;display:flex;align-items:center;padding:0 40px;gap:24px}
.brand{display:flex;align-items:center;gap:8px;font-weight:900;font-size:13px;color:var(--ink)}
.brand-dot{width:34px;height:34px;border-radius:50%;background:var(--orange)}
.nav{display:flex;gap:22px;font-size:9px;font-weight:500;color:var(--ink);margin-left:auto}
.nav span:first-child{border-bottom:2px solid var(--orange)}
.phone{font-size:10px;font-weight:700;color:var(--ink)}
.header-cta{background:var(--orange);width:70px;height:22px}

/* hero */
.hero{top:120px;height:460px}
.hero .ph{position:absolute;inset:0}
.hero-band{position:absolute;left:0;bottom:0;width:100%;height:130px}
.hero-title{position:absolute;left:40px;top:110px;color:var(--white);font-size:24px;font-weight:900;line-height:1.2;text-transform:uppercase;width:380px}
.hero-sub{position:absolute;left:40px;top:175px;color:#eee;font-size:8px;width:320px;line-height:1.5}
.hero .btn{position:absolute;left:40px;top:215px}

/* intro */
.intro{top:580px;height:280px;padding:40px 40px;display:flex;gap:40px}
.intro-text{width:420px}
.eyebrow{font-size:9px;font-weight:700;color:var(--ink);text-transform:uppercase}
.intro h1{font-size:20px;font-weight:900;color:var(--ink);margin:4px 0 12px;text-transform:uppercase}
.intro .btn{margin-top:16px}
.estimate{flex:1;text-align:center}
.estimate .ph{width:150px;height:60px;margin:0 auto 10px;background:linear-gradient(135deg,#eaeaea,#b9b9b9)}
.estimate b{display:block;font-size:11px;color:var(--ink);margin-top:4px}

/* what we do */
.what{top:860px;height:340px;background:var(--grey);padding-top:30px}
.photo-grid{display:grid;grid-template-columns:repeat(3,120px);gap:10px;justify-content:center;margin-top:16px}
.photo-grid .ph{height:90px}

/* pro service */
.pro{top:1200px;height:600px;background:var(--orange)}
.pro .h2{color:var(--white);padding:70px 160px 0;font-size:22px}
.pro .sub{color:var(--white);font-size:9px;font-weight:700;text-align:center;margin-top:12px}
.cards{display:grid;grid-template-columns:repeat(3,160px);gap:40px 36px;justify-content:center;margin-top:40px}
.card{background:var(--white);height:110px;padding:22px 12px 10px;text-align:center;position:relative}
.card::before{content:"";position:absolute;top:-12px;left:66px;width:28px;height:24px;background:var(--white);border:2px solid var(--orange)}
.card b{display:block;font-size:9px;color:var(--ink);text-transform:uppercase;margin-bottom:6px}
.pro .btn{position:absolute;left:370px;top:520px}
.pro svg{position:absolute;left:0;width:100%}

/* before after */
.ba{top:1800px;height:420px;text-align:center;padding-top:30px}
.circles{display:flex;justify-content:center;gap:20px;margin-top:24px;align-items:center;position:relative}
.circles .ph{width:160px;height:160px;border-radius:50%}
.tag{position:absolute;top:60px;background:var(--orange);color:var(--white);font-size:8px;font-weight:700;padding:6px 14px}
.ba .btn{margin-top:24px}

/* pricing */
.price{top:2220px;height:380px;background:var(--grey);display:flex;gap:30px;padding:30px 40px}
.price .ph{width:340px;height:270px}
.price h2{font-size:26px;color:var(--ink);font-weight:700;margin-bottom:14px}
.price li{list-style:none;font-size:8px;line-height:1.5;margin-bottom:7px;padding-left:12px;position:relative}
.price li::before{content:"";position:absolute;left:0;top:3px;width:6px;height:6px;background:var(--orange)}

/* areas */
.areas{top:2600px;height:460px;background:var(--orange);color:var(--white)}
.areas .h2{color:var(--white);padding-top:44px}
.areas .sub{font-size:9px;font-weight:700;text-align:center;margin:10px auto 0;width:400px;line-height:1.4}
.areas-body{display:flex;gap:30px;padding:30px 70px}
.areas-body .txt{width:320px;font-size:8px;line-height:1.55}
.towns{display:grid;grid-template-columns:1fr 1fr;gap:4px;margin-top:16px;font-weight:700;font-size:8px}
.areas-body .ph{width:300px;height:230px;border:4px solid var(--white)}

/* truck */
.truck{top:3060px;height:380px;display:flex;padding:60px 40px;gap:60px}
.truck h2{font-size:22px;color:var(--ink);font-weight:900;text-transform:uppercase;margin-bottom:12px}
.truck-list{flex:1}
.truck-row{display:flex;align-items:center;gap:14px;margin-bottom:16px}
.truck-row .ph{width:100px;height:56px;background:linear-gradient(135deg,#4f6fb0,#26396a)}
.truck-row b{font-size:9px;color:var(--ink);line-height:1.4}

/* steps */
.steps{top:3440px;height:420px;background:var(--grey);text-align:center;padding-top:40px}
.step-row{display:flex;justify-content:center;gap:60px;margin-top:40px}
.step{display:flex;align-items:center;gap:6px}
.num{font-size:72px;font-weight:900;color:var(--orange);line-height:1}
.ring{width:110px;height:110px;border-radius:50%;border:3px solid #bbb;background:var(--white);display:flex;flex-direction:column;align-items:center;justify-content:center;gap:6px;font-size:8px;font-weight:700;color:var(--ink)}

/* contact */
.contact{top:3860px;height:360px;background:var(--orange)}
.contact .h2{color:var(--white);padding-top:36px}
.contact .sub{color:var(--white);font-size:8px;text-align:center;margin-top:8px}
.contact-box{position:absolute;left:120px;top:100px;width:580px;height:230px;background:var(--white);display:flex;padding:16px;gap:16px}
.contact-box .ph{width:260px;height:198px}
.form h3{font-size:16px;color:var(--ink);margin-bottom:10px}
.field{height:20px;border:1px solid #ccc;margin-bottom:8px;width:260px}
.field.tall{height:46px}

/* cta */
.cta{top:4220px;height:180px}
.cta .ph{position:absolute;inset:0}
.cta-text{position:relative;color:var(--white);text-align:center;font-size:15px;line-height:1.3;padding-top:50px;width:460px;margin:0 auto}
.cta .btn{position:absolute;left:366px;top:130px}

/* testimonial */
.reviews{top:4400px;height:500px;text-align:center;padding-top:60px}
.quote{font-size:60px;color:#999;position:absolute;left:100px;top:100px;font-family:Georgia,serif}
.reviews p{width:560px;margin:30px auto 0;font-size:9px;line-height:1.6;font-style:italic}
.avatar{width:36px;height:36px;border-radius:50%;background:#ccc;margin:20px auto 6px}
.stars{color:var(--orange);font-size:12px;letter-spacing:2px}

/* footer */
.site-footer{top:4900px;height:240px;background:var(--ink);color:#ccc;display:flex;padding:40px;gap:50px;font-size:8px}
.site-footer h4{color:var(--white);font-size:9px;margin-bottom:10px}
.site-footer li{list-style:none;margin-bottom:6px}
.copy{position:absolute;bottom:10px;left:0;width:100%;text-align:center;font-size:7px;color:#999}

/* mobile */
.m-block{position:absolute;left:0;width:100%}
.m-pad{padding:14px}
.m-h{font-size:11px;font-weight:900;color:var(--ink);text-transform:uppercase;text-align:center}
.m-card{background:var(--white);height:70px;margin:10px 40px;}
</style>
</head>
<body>

<main class="desktop">
  <header class="site-header">
    <div class="brand"><span class="brand-dot"></span>Bright Creek Junk Out</div>
    <nav class="nav"><span>Home</span><span>Our Services</span><span>What We Do</span><span>Service Areas</span><span>Contact Us</span></nav>
    <div class="phone">(555) 014-2290</div>
    <div class="header-cta"></div>
  </header>

  <section class="hero">
    <div class="ph cool" role="img" aria-label="Photo of a blue dumpster trailer hitched to a white pickup truck"></div>
    <h2 class="hero-title">Junk Removal &amp; Home Cleanout Company</h2>
    <p class="hero-sub">Fast, friendly junk hauling for homes and businesses. We lift, load and haul it all away the same day.</p>
    <span class="btn orange">Call Now</span>
    <svg class="hero-band" viewBox="0 0 812 130" preserveAspectRatio="none"><polygon points="0,60 812,0 812,130 0,130" fill="#fff"/><polygon points="0,50 812,10 812,40 0,90" fill="#f26a0a"/></svg>
  </section>

  <section class="intro">
    <div class="intro-text">
      <div class="eyebrow">Bright Creek Junk Out</div>
      <h1>Junk Removal and Hauling</h1>
      <p class="small">Bright Creek Junk Out offers full service junk removal in the local valley and nearby towns. We are locally owned, fully insured and we treat every home like our own. From a single couch to a full estate cleanout, our crew handles the heavy lifting, sorting, recycling and donation drop off so you do not have to.</p>
      <span class="btn">Learn More</span>
    </div>
    <div class="estimate">
      <div class="ph" role="img" aria-label="Photo of a white pickup truck"></div>
      <b>GET YOUR ESTIMATE NOW</b>
      <p class="small">CALL OR TEXT (555) 014-2290</p>
      <b style="margin-top:14px">BOOK SERVICE NOW</b>
      <p class="small">SEND US YOUR JUNK DETAILS TODAY</p>
      <span class="btn" style="margin-top:10px">Book Online</span>
    </div>
  </section>

  <section class="what">
    <h2 class="h2">What We Do</h2>
    <p class="small center" style="margin-top:6px">From garages to yards, we clear out anything that is in your way.<br>Furniture, appliances, debris and more.</p>
    <div class="photo-grid">
      <div class="ph" role="img" aria-label="Photo of a garage full of junk"></div>
      <div class="ph light" role="img" aria-label="Photo of an empty cleaned room"></div>
      <div class="ph" role="img" aria-label="Photo of a pile of yard debris"></div>
      <div class="ph light" role="img" aria-label="Photo of an old shed"></div>
      <div class="ph" role="img" aria-label="Photo of a demolished shed site"></div>
      <div class="ph dark" role="img" aria-label="Photo of a loaded dump trailer"></div>
    </div>
  </section>

  <section class="pro">
    <svg style="top:0;height:60px" viewBox="0 0 812 60" preserveAspectRatio="none"><polygon points="0,0 812,0 812,10 0,50" fill="#ececec"/></svg>
    <h2 class="h2">Bright Creek's Most Professional Junk Removal Service</h2>
    <p class="sub">WHY YOU SHOULD HIRE BRIGHT CREEK JUNK OUT</p>
    <div class="cards">
      <div class="card"><b>Easy Scheduling</b><p class="small">Book online or call us and we can be there the same or next day.</p></div>
      <div class="card"><b>Upfront Pricing</b><p class="small">Clear quotes based on volume, with no hidden fees or surprises.</p></div>
      <div class="card"><b>All Cleaned Up</b><p class="small">We sweep up after every job and leave the space spotless.</p></div>
      <div class="card"><b>Eco-Friendly Commitment</b><p class="small">We donate and recycle whatever we can to keep it out of landfills.</p></div>
      <div class="card"><b>Professional Service</b><p class="small">Our uniformed, insured crew is friendly, careful and on time.</p></div>
      <div class="card"><b>3 Payment Methods</b><p class="small">Pay by card, cash or check, whichever suits you best.</p></div>
    </div>
    <span class="btn">Free Quote</span>
    <svg style="bottom:0;height:50px" viewBox="0 0 812 50" preserveAspectRatio="none"><polygon points="0,50 812,0 812,50" fill="#fff"/></svg>
  </section>

  <section class="ba">
    <h2 class="h2">Before After</h2>
    <p class="small" style="width:520px;margin:8px auto 0">See the difference a single visit makes. Real jobs from our crew, cleared out in a few hours and left clean and ready to use again.</p>
    <div class="circles">
      <span class="tag" style="left:170px">BEFORE</span>
      <div class="ph" role="img" aria-label="Before photo of a cluttered room"></div>
      <div class="ph light" role="img" aria-label="After photo of the same room cleared"></div>
      <span class="tag" style="right:170px">AFTER</span>
    </div>
    <span class="btn">Learn More</span>
  </section>

  <section class="price">
    <div class="ph" role="img" aria-label="Photo of a room filled with household junk"></div>
    <div>
      <h2>HOW WE PRICE</h2>
      <ul>
        <li><b>Volume Based Pricing.</b> Your price is set by how much space your items take up in our trailer.</li>
        <li><b>Minimum Loads.</b> Small pickups start at a low flat minimum charge.</li>
        <li><b>Free Estimates.</b> We give on-site quotes before any work begins.</li>
        <li><b>Special Pricing.</b> Heavy items like concrete or dirt are priced by weight.</li>
        <li><b>No Hidden Fees.</b> Labor, loading and disposal are all included.</li>
      </ul>
      <span class="btn orange" style="margin-top:10px">Free Quote</span>
    </div>
  </section>

  <section class="areas">
    <h2 class="h2">Service Areas</h2>
    <p class="sub">BRIGHT CREEK JUNK OUT PROUDLY SERVES THE WHOLE VALLEY AND THE TOWNS AROUND IT</p>
    <div class="areas-body">
      <div class="txt">
        <p>Bright Creek Junk Out is a locally owned hauling team serving homeowners, landlords, realtors and businesses across the valley. If you do not see your town listed below, give us a call and ask. We travel often and are happy to help wherever we can.</p>
        <div class="towns"><span>• Northfield</span><span>• Cedar Park</span><span>• Millbrook</span><span>• Ashby</span><span>• Lakeview</span><span>• Stonebridge</span><span>• Elm Grove</span><span>• Riverside</span></div>
      </div>
      <div class="ph" role="img" aria-label="Photo of crew loading boxes into a trailer"></div>
    </div>
  </section>

  <section class="truck">
    <div style="width:300px">
      <h2>Bigger Truck Better Price</h2>
      <p class="small">Our trailer holds more per load than a standard pickup, so you get more space for your money and fewer trips to finish the job.</p>
      <span class="btn" style="margin-top:14px">Learn More</span>
    </div>
    <div class="truck-list">
      <div class="truck-row"><div class="ph" role="img" aria-label="Photo of pickup trucks"></div><b>3 pickup loads<br>OR 1 trailer load<br>15 cubic yards</b></div>
      <div class="truck-row"><div class="ph" role="img" aria-label="Photo of pickup trucks"></div><b>4 pickup loads<br>OR 1 trailer load<br>20 cubic yards</b></div>
      <div class="truck-row"><div class="ph" role="img" aria-label="Photo of pickup trucks"></div><b>5 pickup loads<br>OR 1 trailer load<br>25 cubic yards</b></div>
    </div>
  </section>

  <section class="steps">
    <h2 class="h2">3 Simple Way To Get You Estimate</h2>
    <p class="small" style="width:460px;margin:8px auto 0">Pick the option that works best for you and we will get back with a quote fast.</p>
    <div class="step-row">
      <div class="step"><span class="num">1</span><div class="ring"><svg width="22" height="22" viewBox="0 0 24 24"><path d="M6 2h4l2 5-3 2a11 11 0 0 0 6 6l2-3 5 2v4a2 2 0 0 1-2 2A18 18 0 0 1 4 4a2 2 0 0 1 2-2z" fill="#141414"/></svg>CALL TO BOOK</div></div>
      <div class="step"><span class="num">2</span><div class="ring"><svg width="22" height="22" viewBox="0 0 24 24"><rect x="3" y="4" width="18" height="13" rx="2" fill="#141414"/><polygon points="7,17 7,21 11,17" fill="#141414"/></svg>TEXT A PHOTO</div></div>
      <div class="step"><span class="num">3</span><div class="ring"><svg width="22" height="22" viewBox="0 0 24 24"><rect x="3" y="5" width="18" height="14" rx="1" fill="none" stroke="#141414" stroke-width="2"/><polyline points="3,6 12,13 21,6" fill="none" stroke="#141414" stroke-width="2"/></svg>BOOK ONLINE</div></div>
    </div>
  </section>

  <section class="contact">
    <h2 class="h2">Contact Us</h2>
    <p class="sub">Reach out any time and our team will reply within a single business day.</p>
    <div class="contact-box">
      <div class="ph map" role="img" aria-label="Map of the service area"></div>
      <div class="form">
        <h3>GET IN TOUCH</h3>
        <div class="field"></div><div class="field"></div><div class="field"></div><div class="field tall"></div>
        <span class="btn">Submit</span>
      </div>
    </div>
  </section>

  <section class="cta">
    <div class="ph dark" role="img" aria-label="Photo of the crew loading junk at dusk"></div>
    <p class="cta-text">your professional &amp; friendly junk removal experts.<br>you call, we haul! we'll solve all your junk removal &amp; property cleanout problems.</p>
    <span class="btn orange">Call Now</span>
  </section>

  <section class="reviews">
    <h2 class="h2">Testimonial</h2>
    <span class="quote">“</span>
    <p>“The crew showed up on time, were friendly and professional, and cleared out our whole garage in under two hours. Great price and they even swept up. I will be calling them again.”</p>
    <div class="avatar"></div>
    <div class="small"><b>Jordan Ellis</b></div>
    <div class="stars">★★★★★</div>
  </section>

  <footer class="site-footer">
    <div class="brand" style="color:#fff;flex-direction:column;align-items:flex-start;width:150px"><span class="brand-dot"></span>Bright Creek Junk Out</div>
    <div><h4>QUICK LINKS</h4><ul><li>Home</li><li>Our Services</li><li>What We Do</li><li>Service Areas</li></ul></div>
    <div><h4>SERVICE AREAS</h4><ul><li>Northfield</li><li>Cedar Park</li><li>Millbrook</li><li>Lakeview</li></ul></div>
    <div><h4>CONTACTUS</h4><ul><li>(555) 014-2290</li><li>BrightCreekJunkOut.com</li><li>Open Mon – Sat</li></ul></div>
    <p class="copy">COPYRIGHT © BRIGHT CREEK JUNK OUT</p>
  </footer>
</main>

<aside class="mobile">
  <div class="m-block" style="top:0;height:60px;display:flex;align-items:center;padding:0 12px;gap:6px"><span class="brand-dot" style="width:22px;height:22px"></span><b style="font-size:8px;color:var(--ink)">Bright Creek Junk Out</b></div>
  <div class="m-block ph cool" style="top:60px;height:200px" role="img" aria-label="Photo of a dumpster trailer and truck"></div>
  <div class="m-block" style="top:180px;height:80px;background:var(--orange)"></div>
  <div class="m-block m-pad" style="top:270px"><p class="m-h">Junk Removal and Hauling</p><p class="small" style="margin-top:6px">Full service junk removal for homes and businesses across the valley. Fast, friendly and insured.</p></div>
  <div class="m-block m-pad center" style="top:400px"><div class="ph" style="height:70px;margin:0 50px" role="img" aria-label="Photo of a white pickup truck"></div><p class="small" style="margin-top:6px"><b>GET YOUR ESTIMATE NOW</b></p></div>
  <div class="m-block" style="top:530px;height:320px;background:var(--grey);padding:14px"><p class="m-h">What We Do</p>
    <div style="display:grid;grid-template-columns:1fr 1fr;gap:6px;margin-top:10px"><div class="ph" style="height:60px" role="img" aria-label="Photo of junk"></div><div class="ph light" style="height:60px" role="img" aria-label="Photo of a cleared room"></div><div class="ph" style="height:60px" role="img" aria-label="Photo of a shed"></div><div class="ph dark" style="height:60px" role="img" aria-label="Photo of a trailer"></div></div></div>
  <div class="m-block" style="top:850px;height:900px;background:var(--orange);padding-top:20px"><p class="m-h" style="color:#fff;padding:0 20px">Bright Creek's Most Professional Junk Removal Service</p>
    <div class="m-card"></div><div class="m-card"></div><div class="m-card"></div><div class="m-card"></div><div class="m-card"></div><div class="m-card"></div></div>
  <div class="m-block m-pad" style="top:1760px"><p class="m-h">What We Do</p><div class="ph" style="height:120px;margin-top:10px" role="img" aria-label="Before and after photos"></div></div>
  <div class="m-block m-pad" style="top:2110px;background:var(--grey);height:430px"><p class="m-h">How We Price</p><p class="small" style="margin-top:8px">Volume based pricing, free estimates, low minimum loads and no hidden fees.</p><div class="ph" style="height:130px;margin-top:12px" role="img" aria-label="Photo of a room filled with junk"></div></div>
  <div class="m-block" style="top:2540px;height:420px;background:var(--orange);padding:16px"><p class="m-h" style="color:#fff">Service Areas</p><p class="small" style="color:#fff;margin-top:8px">Serving Northfield, Cedar Park, Millbrook, Ashby, Lakeview and nearby towns.</p><div class="ph" style="height:120px;margin-top:20px" role="img" aria-label="Photo of crew loading boxes"></div></div>
  <div class="m-block m-pad" style="top:2980px"><p class="m-h">Bigger Truck Better Price</p><div class="ph" style="height:40px;margin:10px 40px 0;background:linear-gradient(135deg,#4f6fb0,#26396a)" role="img" aria-label="Photo of pickup trucks"></div><div class="ph" style="height:40px;margin:8px 40px 0;background:linear-gradient(135deg,#4f6fb0,#26396a)" role="img" aria-label="Photo of pickup trucks"></div><div class="ph" style="height:40px;margin:8px 40px 0;background:linear-gradient(135deg,#4f6fb0,#26396a)" role="img" aria-label="Photo of pickup trucks"></div></div>
  <div class="m-block m-pad center" style="top:3260px;background:var(--grey);height:520px"><p class="m-h">3 Simple Way To Get You Estimate</p>
    <div style="display:flex;flex-direction:column;align-items:center;gap:18px;margin-top:18px"><div class="step"><span class="num" style="font-size:50px">1</span><div class="ring" style="width:80px;height:80px">CALL</div></div><div class="step"><span class="num" style="font-size:50px">2</span><div class="ring" style="width:80px;height:80px">TEXT</div></div><div class="step"><span class="num" style="font-size:50px">3</span><div class="ring" style="width:80px;height:80px">ONLINE</div></div></div></div>
  <div class="m-block" style="top:3780px;height:300px;background:var(--orange);padding:16px"><p class="m-h" style="color:#fff">Contact Us</p><div class="ph map" style="height:200px;margin-top:12px" role="img" aria-label="Map of the service area"></div></div>
  <div class="m-block m-pad" style="top:4090px"><p class="m-h" style="text-align:left">Get In Touch</p><div class="field" style="width:100%;margin-top:8px"></div><div class="field" style="width:100%"></div><div class="field tall" style="width:100%"></div><span class="btn">Submit</span></div>
  <div class="m-block ph dark" style="top:4290px;height:200px" role="img" aria-label="Photo of the crew at work"></div>
  <div class="m-block m-pad center" style="top:4500px"><p class="m-h">Testimonial</p><p class="small" style="margin-top:6px">“On time, friendly and fast. Great price.”</p><div class="stars">★★★★★</div></div>
  <div class="m-block" style="top:4620px;height:390px;background:var(--ink);padding:20px;color:#ccc;font-size:8px"><div class="brand" style="color:#fff"><span class="brand-dot" style="width:24px;height:24px"></span>Bright Creek Junk Out</div><p style="margin-top:20px;color:#fff;font-weight:700">QUICK LINKS</p><p style="margin-top:6px">Home · Services · What We Do · Areas</p><p style="margin-top:20px;color:#fff;font-weight:700">CONTACT US</p><p style="margin-top:6px">(555) 014-2290</p><p>BrightCreekJunkOut.com</p></div>
</aside>

</body>
</html>
```